refresh/modernization of affiliate website template

Make this website look better. The site is comprised of various sections (nav, hero, products, FAQ, testimonials, gallery, contact us, blog listing page, single post page) that are modular in nature and it would be great if the genera template of the site was reusable with industries other than travel. We left the "look and feel" sliders in the neutral position because we are not too sure what we want and thus would like to see various approaches.

Number of Pages Required

3 page

```html
<!DOCTYPE html>
<html lang="en">
<head>
<meta charset="utf-8">
<title>Wander Well – The Importance of a Travel Medicine Bag</title>
<link href="https://fonts.googleapis.com/css2?family=Poppins:wght@300;400;500;600;700&display=swap" rel="stylesheet">
<style>
:root{
  --purple:#5a12f0;
  --purple-dark:#3b1a8c;
  --text:#4a4a4a;
  --heading:#333333;
  --muted:#b9b9b9;
  --tag:#a6e5e1;
  --pink:#e0357f;
  --footer:#272261;
  --white:#ffffff;
}
*{margin:0;padding:0;box-sizing:border-box}
html,body{width:886px;height:1200px;overflow:hidden;background:var(--white)}
body{font-family:'Poppins',sans-serif;color:var(--text);position:relative}

.hero{position:absolute;left:0;top:0;width:886px;height:145px;
  background:linear-gradient(170deg,#5f8a86 0%,#8fb3ae 30%,#d9e2e0 55%,#f2c9ae 80%,#f6c7a8 100%)}
.brand{position:absolute;top:10px;width:100%;text-align:center;color:var(--white);font-weight:600;font-size:18px;letter-spacing:.2px}
.nav{position:absolute;top:42px;width:100%;display:flex;justify-content:center;gap:0;font-size:8px;color:var(--white);font-weight:400}
.nav span{margin:0 11px}
.nav span.gap{margin-left:14px}
.page-title{position:absolute;top:86px;width:100%;text-align:center;color:var(--purple);font-weight:700;font-size:25px}

.article{position:absolute;left:180px;top:219px;width:524px}
.article-photo{float:left;width:197px;height:226px;border-radius:10px;margin:0 19px 4px 0;
  background:linear-gradient(135deg,#c98a4a 0%,#d9a268 40%,#b77a3d 100%)}
.article-title{font-size:15.5px;font-weight:500;color:var(--heading);padding-top:10px;line-height:19px}
.meta{font-size:8px;color:var(--muted);margin-top:2px}
.tag-row{display:flex;justify-content:space-between;align-items:center;margin-top:4px;margin-bottom:19px}
.tag{background:var(--tag);color:var(--white);font-size:8px;width:55px;height:13px;line-height:13px;text-align:center}
.share{display:flex;align-items:center;gap:5px;font-size:8px;color:#666}
.share i{display:block;width:14px;height:14px;border-radius:50%;background:var(--purple)}
.article p{font-size:8px;line-height:12px;font-weight:300;color:var(--text);margin-bottom:12px}

.btn{position:absolute;height:23px;border:1px solid var(--pink);border-radius:12px;color:var(--purple);
  font-size:8px;font-weight:400;display:flex;align-items:center;justify-content:center;background:var(--white)}
.btn-shop{left:355px;top:715px;width:177px}
.btn-back{left:374px;top:904px;width:138px}

.post-card{position:absolute;top:770px;width:268px;height:115px;border-radius:8px;overflow:hidden;padding:18px 28px}
.post-card.prev{left:171px;background:linear-gradient(120deg,#4b2a9a,#3a1580 60%,#2f0f70)}
.post-card.next{left:448px;background:linear-gradient(120deg,#5c3aa8,#5331a0 60%,#4a2a92)}
.post-label{font-size:9px;font-weight:600;color:#b7a6e6}
.post-title{font-size:15.5px;line-height:18.5px;font-weight:600;color:var(--white);margin-top:2px}

.footer{position:absolute;left:0;top:972px;width:886px;height:228px;
  background:linear-gradient(160deg,#2b2a6e 0%,#272261 50%,#35297a 100%);color:var(--white)}
.footer-brand{position:absolute;left:169px;top:33px;font-size:17.5px;font-weight:600}
.footer-about{position:absolute;left:169px;top:67px;width:190px;font-size:8.6px;line-height:12px}
.follow{position:absolute;left:169px;top:141px;font-size:7.5px;font-weight:600}
.social{position:absolute;left:171px;top:156px;display:flex;gap:8px}
.social i{display:block;width:18px;height:18px;border-radius:50%;background:#d8d6e6}
.col{position:absolute;top:46px;font-size:8.6px}
.col h4{font-size:8.6px;font-weight:600;margin-bottom:5px}
.col li{list-style:none;color:#d7d4ee;height:16.6px}
.col-explore{left:427px}
.col-company{left:531px;top:45px}
.col-resources{left:637px;top:45px}
.divider{position:absolute;left:169px;top:197px;width:545px;height:1px;background:#5a5690}
.site-url{position:absolute;top:208px;width:100%;text-align:center;font-size:8px;color:#e6e4f4}
</style>
</head>
<body>

<header class="hero" role="img" aria-label="Aerial photo of ocean waves washing over a sandy beach">
  <div class="brand">Wander Well</div>
  <nav class="nav">
    <span>Features</span><span>Travel Tips &amp; Answers</span><span>Products</span><span>FAQs</span><span>Testimonials</span><span>Gallery</span><span class="gap">Contact Us</span>
  </nav>
  <h1 class="page-title">Travel Tips &amp; Answers</h1>
</header>

<article class="article">
  <div class="article-photo" role="img" aria-label="Traveler packing rolled clothes, pouches and a camera on a wooden floor"></div>
  <h2 class="article-title">The Importance of a Travel Medicine Bag</h2>
  <div class="meta">24 Sep, 2023 &nbsp;-&nbsp; 5 min read</div>
  <div class="tag-row">
    <span class="tag">Health</span>
    <div class="share">Share: <i></i><i></i><i></i></div>
  </div>
  <p>Traveling can be an exciting and enriching experience, but it's important to prioritize your health and safety while on the go. One essential item that should be part of every traveler's checklist is a reliable travel medicine bag.</p>
  <p>A travel medicine bag, like the Velora Pill Case Organizer Bag, is designed to keep your medications, vitamins, and other medical supplies organized and easily accessible. It offers several benefits and plays a crucial role in ensuring a worry-free journey.</p>
  <p>First and foremost, a travel medicine bag provides convenience. When you're away from home, it's easy to forget to pack all the necessary medications and supplements. Having a designated bag to store your pills and medical accessories eliminates the risk of leaving anything behind. Plus, with its various compartments and mesh pouches, you can keep everything neatly organized, making it easy to find what you need, when you need it. Another significant advantage of a travel medicine bag is its durability. The Velora Pill Case Organizer Bag is made from water-resistant, lightweight fabric, ensuring that your medications are protected from moisture and other external factors. It is well-padded to offer additional cushioning and safeguard your pill bottles from any potential damage.</p>
  <p>Safety is paramount when it comes to medication, especially when traveling. The Velora Pill Case Organizer Bag is equipped with a dual-zipper that can be locked, providing an extra layer of security. This is especially important when traveling to unfamiliar places where the safety and integrity of your medications may be a concern. Additionally, the ID card window on the bag allows for quick access to important medical records in case of emergencies.</p>
  <p>Lastly, a travel medicine bag promotes peace of mind. Knowing that you have all your medications and supplies organized and readily available can alleviate any anxiety or stress that may come with traveling. Whether you're embarking on a family vacation or a solo adventure, having a well-stocked and functional travel medicine bag ensures that you can address any health-related issues that may arise during your trip.</p>
  <p>In conclusion, a travel medicine bag, such as the Velora Pill Case Organizer Bag, is an indispensable tool for any traveler. Its convenience, durability, safety features, and peace of mind it offers make it an essential item to include in your travel essentials checklist. Prioritizing your health and well-being while traveling is crucial and a travel medicine bag helps you do just that. So, before your next journey, invest in a reliable travel medicine bag and travel with confidence.</p>
</article>

<a class="btn btn-shop">Get Your Own Travel Medicine Bag</a>

<div class="post-card prev" role="img" aria-label="Hands packing a toiletry pouch, tinted purple">
  <div class="post-label">Prev Article</div>
  <div class="post-title">How to Keep your Toiletries Secure and Mess-Free While Traveling</div>
</div>
<div class="post-card next" role="img" aria-label="Traveler carrying a dog in a pet carrier, tinted purple">
  <div class="post-label">Next Article</div>
  <div class="post-title">How to Choose the Right Pet Carrier for Air Travel</div>
</div>

<a class="btn btn-back">Back to Articles</a>

<footer class="footer" role="contentinfo" aria-label="Footer over a photo of a surfer riding a wave at dusk">
  <div class="footer-brand">Wander Well</div>
  <p class="footer-about">Lorem ipsum dolor sit amet, con sectetur adipiscing elit, sed do eiusmod tempor incididunt ut labore et dolore magna</p>
  <div class="follow">Follow Us On Social Media</div>
  <div class="social"><i></i><i></i><i></i><i></i><i></i></div>
  <ul class="col col-explore"><h4>Explore</h4><li>Features</li><li>Travel Tips</li><li>Answers</li><li>Products</li><li>Gallery</li></ul>
  <ul class="col col-company"><h4>Company</h4><li>Our Story</li><li>Contact Us</li><li>Careers</li><li>Legal</li></ul>
  <ul class="col col-resources"><h4>Resources</h4><li>Testimonials</li><li>Blog</li><li>Help Center</li><li>FAQ</li></ul>
  <div class="divider"></div>
  <div class="site-url">www.wanderwell.example</div>
</footer>

</body>
</html>
```